Voltline Assemblies, Inc. Business Card

Voltline has three operating entities and I'm looking for a standard business card template that can be used for Voltline and the three operating entities that the logo just get swapped out, but has a very similar look and feel. Ultimately if someone had a business card from each, they assume the organizations are related because they all have the same look and feel.
Below are our websites and I will attached the logos for each entity:
https://www.voltlineassemblies.example/
https://www.brantoceramic.example/
https://www.omra-kfsd.example/
https://www.summitbreaker.example/

Target Market(s)

US Voltline

Industry/Entity Type

US Voltline

Contact Information for Business Card

Normal stuff

```html
<!DOCTYPE html>
<html lang="en">
<head>
<meta charset="utf-8">
<title>Voltline Assemblies – Business Card Family</title>
<link href="https://fonts.googleapis.com/css2?family=Roboto:wght@400;500;700&display=swap" rel="stylesheet">
<style>
  :root{
    --navy:#1f2a6b;
    --red:#d0202e;
    --sky:#4f86c6;
    --grey:#7a7a7a;
    --steel:#4c7a96;
    --charcoal:#2f2f2f;
    --ink:#222;
    --paper:#fff;
  }
  *{box-sizing:border-box;margin:0;padding:0}
  html,body{width:966px;height:1200px;overflow:hidden}
  body{
    font-family:"Roboto",Arial,sans-serif;
    background:radial-gradient(ellipse at 50% 50%,#ececec 0%,#d6d6d6 55%,#bdbdbd 100%);
    position:relative;
  }
  .card{
    position:absolute;width:446px;height:255px;background:var(--paper);
    border-radius:9px;overflow:hidden;
    box-shadow:0 3px 8px rgba(0,0,0,.28);
  }
  .col-front{left:27px}
  .col-back{left:499px}
  .row-1{top:40px}.row-2{top:330px}.row-3{top:618px}.row-4{top:908px}

  .brand-voltline{--main:var(--navy);--accent:var(--red);--band-a:var(--navy);--band-b:var(--red)}
  .brand-branto{--main:var(--navy);--accent:var(--sky);--band-a:var(--navy);--band-b:#5b8fd0}
  .brand-omra{--main:var(--navy);--accent:var(--grey);--band-a:var(--navy);--band-b:#6f6f6f}
  .brand-summit{--main:var(--steel);--accent:var(--ink);--band-a:var(--steel);--band-b:var(--charcoal)}

  /* wordmark */
  .wordmark{position:absolute;display:flex;flex-direction:column;align-items:center;color:var(--main)}
  .wordmark-line{display:flex;align-items:center;gap:7px}
  .wordmark-dot{width:16px;height:16px;border-radius:50%;background:var(--main);flex:none}
  .wordmark-square{border-radius:3px}
  .wordmark-name{font-weight:700;font-size:17px;letter-spacing:.2px;white-space:nowrap}
  .wordmark-parent{font-size:7px;font-weight:500;margin-top:3px;white-space:nowrap}
  .col-front .wordmark{right:22px;top:80px}
  .col-back .wordmark{left:50%;top:136px;transform:translateX(-50%)}
  .col-back .wordmark-name{font-size:21px}
  .col-back .wordmark-dot{width:20px;height:20px}
  .col-back .wordmark-parent{font-size:8.5px}

  /* front details */
  .person{position:absolute;left:22px;top:151px}
  .person-name{font-size:11.5px;font-weight:700;color:var(--main);letter-spacing:.2px}
  .person-title{font-size:10.5px;color:var(--accent);margin-top:1px}
  .rule{position:absolute;left:22px;right:22px;top:184px;height:1px;background:var(--main)}
  .address{position:absolute;left:22px;top:191px;font-size:10px;line-height:14.4px;color:var(--ink);font-style:normal}
  .address-company{color:var(--main);font-weight:500}
  .contact{position:absolute;right:22px;top:191px;font-size:10px;line-height:14.4px;color:var(--ink);text-align:right;list-style:none}
  .contact li{display:flex;justify-content:flex-end;align-items:center;gap:3px}
  .contact svg{width:7px;height:7px;fill:var(--main);color:var(--main)}

  .band{position:absolute;left:0;bottom:0;width:446px;height:8px;display:block}
  .seg-a{fill:var(--band-a)}
  .seg-b{fill:var(--band-b)}

  .site{position:absolute;left:0;right:0;top:229px;text-align:center;font-size:10.5px;color:var(--ink);letter-spacing:.2px}
  .site strong{font-weight:500;color:var(--main)}
</style>
</head>
<body>
<svg width="0" height="0" style="position:absolute">
  <defs>
    <symbol id="icon-phone" viewBox="0 0 10 10"><path d="M2 .5 3.6 2.4 2.7 3.5C3.3 4.9 5.1 6.7 6.5 7.3L7.6 6.4 9.5 8 8.6 9.3C5 9.6.4 5 .7 1.4Z"/></symbol>
    <symbol id="icon-mail" viewBox="0 0 10 10"><path d="M.5 2h9v6h-9Z"/><path d="M.8 2.3 5 5.6 9.2 2.3" fill="none" stroke="#fff" stroke-width=".8"/></symbol>
    <symbol id="icon-globe" viewBox="0 0 10 10"><circle cx="5" cy="5" r="4.5"/><path d="M.5 5h9M5 .5v9M2 2.5h6M2 7.5h6" stroke="#fff" stroke-width=".7" fill="none"/></symbol>
  </defs>
</svg>

<!-- Voltline -->
<article class="card col-front row-1 brand-voltline">
  <div class="wordmark"><div class="wordmark-line"><span class="wordmark-dot"></span><span class="wordmark-name">Voltline Assemblies, Inc.</span></div></div>
  <div class="person"><p class="person-name">DANIEL HARTWELL</p><p class="person-title">President</p></div>
  <div class="rule"></div>
  <address class="address"><p class="address-company">Voltline Assemblies INC.</p><p>1840 Ridgeview Drive</p><p>Suite 210, Fairhaven, AL 35000</p></address>
  <ul class="contact">
    <li>555 014 2290<svg><use href="#icon-phone"/></svg></li>
    <li>info@voltlineassemblies.example<svg><use href="#icon-mail"/></svg></li>
    <li>www.voltlineassemblies.example<svg><use href="#icon-globe"/></svg></li>
  </ul>
  <svg class="band" viewBox="0 0 446 8" preserveAspectRatio="none"><polygon class="seg-a" points="0,0 232,0 222,8 0,8"/><polygon class="seg-b" points="238,0 446,0 446,8 228,8"/></svg>
</article>
<article class="card col-back row-1 brand-voltline">
  <div class="wordmark"><div class="wordmark-line"><span class="wordmark-dot"></span><span class="wordmark-name">Voltline Assemblies, Inc.</span></div></div>
  <p class="site">www.<strong>voltlineassemblies</strong>.example</p>
</article>

<!-- Branto -->
<article class="card col-front row-2 brand-branto">
  <div class="wordmark"><div class="wordmark-line"><span class="wordmark-dot"></span><span class="wordmark-name">Branto Ceramic, LLC</span></div><p class="wordmark-parent">A Voltline Assemblies, Inc. Company</p></div>
  <div class="person"><p class="person-name">DANIEL HARTWELL</p><p class="person-title">President</p></div>
  <div class="rule"></div>
  <address class="address"><p class="address-company">Branto Ceramic, LLC</p><p>412 W. County Rd 9, Ste 2,</p><p>PO Box 71, Lindale OH, USA, 44000</p></address>
  <ul class="contact">
    <li>1 (555) 010-4471<svg><use href="#icon-phone"/></svg></li>
    <li>info@brantoceramic.example<svg><use href="#icon-mail"/></svg></li>
    <li>www.brantoceramic.example<svg><use href="#icon-globe"/></svg></li>
  </ul>
  <svg class="band" viewBox="0 0 446 8" preserveAspectRatio="none"><polygon class="seg-a" points="0,0 232,0 222,8 0,8"/><polygon class="seg-b" points="238,0 446,0 446,8 228,8"/></svg>
</article>
<article class="card col-back row-2 brand-branto">
  <div class="wordmark"><div class="wordmark-line"><span class="wordmark-dot"></span><span class="wordmark-name">Branto Ceramic, LLC</span></div><p class="wordmark-parent">A Voltline Assemblies, Inc. Company</p></div>
  <p class="site">www.<strong>brantoceramic</strong>.example</p>
</article>

<!-- OMRA -->
<article class="card col-front row-3 brand-omra">
  <div class="wordmark"><div class="wordmark-line"><span class="wordmark-dot wordmark-square"></span><span class="wordmark-name">OMRA</span></div><p class="wordmark-parent">A Voltline Assemblies, Inc. Company</p></div>
  <div class="person"><p class="person-name">DANIEL HARTWELL</p><p class="person-title">President</p></div>
  <div class="rule"></div>
  <address class="address"><p class="address-company">OMRA, Inc.</p><p>PO Box 306</p><p>Harlow, NC 28000</p></address>
  <ul class="contact">
    <li>1 (555) 013-8820<svg><use href="#icon-phone"/></svg></li>
    <li>info@omra-kfsd.example<svg><use href="#icon-mail"/></svg></li>
    <li>www.omra-kfsd.example<svg><use href="#icon-globe"/></svg></li>
  </ul>
  <svg class="band" viewBox="0 0 446 8" preserveAspectRatio="none"><polygon class="seg-a" points="0,0 232,0 222,8 0,8"/><polygon class="seg-b" points="238,0 446,0 446,8 228,8"/></svg>
</article>
<article class="card col-back row-3 brand-omra">
  <div class="wordmark"><div class="wordmark-line"><span class="wordmark-dot wordmark-square"></span><span class="wordmark-name">OMRA</span></div><p class="wordmark-parent">A Voltline Assemblies, Inc. Company</p></div>
  <p class="site">www.<strong>omra-kfsd</strong>.example</p>
</article>

<!-- Summit -->
<article class="card col-front row-4 brand-summit">
  <div class="wordmark"><div class="wordmark-line"><span class="wordmark-dot"></span><span class="wordmark-name">SUMMIT BREAKER</span></div><p class="wordmark-parent">A Voltline Assemblies Inc. Company</p></div>
  <div class="person"><p class="person-name">DANIEL HARTWELL</p><p class="person-title">President</p></div>
  <div class="rule"></div>
  <address class="address"><p class="address-company">Summit Breaker</p><p>7720 Cedar Row SE Fairhaven,</p><p>AL 35000</p></address>
  <ul class="contact">
    <li>1 (555) 010-4471<svg><use href="#icon-phone"/></svg></li>
    <li>info@brantoceramic.example<svg><use href="#icon-mail"/></svg></li>
    <li>www.brantoceramic.example<svg><use href="#icon-globe"/></svg></li>
  </ul>
  <svg class="band" viewBox="0 0 446 8" preserveAspectRatio="none"><polygon class="seg-a" points="0,0 232,0 222,8 0,8"/><polygon class="seg-b" points="238,0 446,0 446,8 228,8"/></svg>
</article>
<article class="card col-back row-4 brand-summit">
  <div class="wordmark"><div class="wordmark-line"><span class="wordmark-dot"></span><span class="wordmark-name">SUMMIT BREAKER</span></div><p class="wordmark-parent">A Voltline Assemblies Inc. Company</p></div>
  <p class="site">www.<strong>summitbreaker</strong>.example</p>
</article>
</body>
</html>
```